KPFT website

The design should be based on the style and layout of the Tevix website (https://www.tevixorb.ae/about-us) , incorporating softer tones.
Use KPFT green for headers and ash grey for other elements to maintain brand consistency.
The top of the homepage should include a dynamic counter that displays the number of projects we are currently working on and their total value.

Then going into Who we are, Vision, Mission, Directors, Our Values then Current Projects.
The current project wont link to any where right now but would like this option later on.

The bottom of the homepage should feature a section dedicated to showcasing the logos or names of our key clients.

This website will be an essential tool for communicating our expertise and engaging with potential clients, so it should be visually appealing, user-friendly, and aligned with our brand identity.

```html
<!DOCTYPE html>
<html lang="en">
<head>
<meta charset="utf-8">
<title>KPFT – Project &amp; Cost Management Consultancy</title>
<link href="https://fonts.googleapis.com/css2?family=Krona+One&family=Roboto:wght@400;500;700&display=swap" rel="stylesheet">
<style>
:root{
  --green:#0f8a6b;
  --green-dark:#0b7559;
  --ash:#46494c;
  --ash-dark:#3c3f42;
  --ink:#1d1d1d;
  --text:#555a5e;
  --light:#f3f3f3;
  --white:#fff;
}
*{margin:0;padding:0;box-sizing:border-box}
html,body{width:1200px;height:4354px;overflow:hidden}
body{position:relative;font-family:"Roboto",sans-serif;color:var(--text);background:var(--white)}
.abs{position:absolute}
.heading{font-family:"Krona One",sans-serif;font-size:33px;color:var(--ink);letter-spacing:-0.5px;font-weight:400}
.heading span{color:var(--green)}

/* header */
.site-header{left:0;top:0;width:1200px;height:58px}
.logo-area{left:0;top:0;width:380px;height:58px;background:var(--white)}
.logo{left:111px;top:10px;font-family:"Krona One",sans-serif;font-size:32px;color:var(--green);letter-spacing:2px}
.main-nav{left:380px;top:0;width:820px;height:58px;background:var(--green);display:flex;align-items:center;padding-left:35px;gap:24px;font-size:12.5px;color:var(--white);font-weight:500}
.main-nav .active{text-decoration:underline}
.nav-phone{margin-left:auto;margin-right:95px;display:flex;align-items:center;gap:8px}

/* hero */
.hero{left:0;top:58px;width:1200px;height:557px;background:linear-gradient(90deg,#5d6a78 0%,#8d9bab 30%,#c7d2dc 60%,#eef2f5 80%,#f6f8f9 100%)}
.hero-text{right:113px;top:133px;text-align:right}
.hero-welcome{font-size:21px;color:var(--ink)}
.hero-title{font-family:"Krona One",sans-serif;font-size:36px;line-height:56px;color:var(--ink);margin-top:6px}
.hero-title span{color:var(--green)}
.hero-lead{font-size:13px;line-height:28px;color:var(--ink);margin-top:10px}
.btn{display:inline-block;border-radius:22px;color:var(--white);font-weight:500;font-size:14.5px}
.btn-green{background:var(--green);padding:12px 32px;margin-top:16px}
.dots{left:577px;top:542px;display:flex;gap:5px}
.dots i{width:12px;height:12px;border-radius:50%;background:var(--white);display:block}
.dots i.on{background:var(--green);border:2px solid #fff}

/* counters */
.counter{top:615px;height:71px;display:flex;align-items:center;justify-content:center;font-family:"Krona One",sans-serif;font-size:22px;color:var(--white)}
.counter-projects{left:0;width:603px;background:var(--ash)}
.counter-value{left:603px;width:597px;background:var(--green)}

/* text sections */
.section-text{left:111px;width:980px;font-size:13px;line-height:28px}
.quote{font-family:Georgia,serif;font-size:28px;color:var(--ink);line-height:0}
.btn-ash{background:var(--ash);padding:13px 34px}

/* values */
.values{left:0;top:1648px;width:1200px;height:502px;background:linear-gradient(135deg,#3f4245 0%,#55585b 45%,#45484b 100%)}
.value{width:330px;color:var(--white)}
.value h3{display:flex;align-items:center;gap:10px;font-size:19px;font-weight:400}
.value p{font-size:13px;line-height:24px;margin-top:16px;color:#e2e2e2;padding-left:6px}

/* directors */
.director{width:220px;text-align:center}
.photo{width:192px;height:192px;border-radius:50%;margin:0 auto;background:radial-gradient(circle at 50% 40%,#f4f4f4 0%,#d9d9d9 60%,#bdbdbd 100%)}
.director.chair .photo{border:3px solid var(--green)}
.director h4{font-size:19px;font-weight:400;color:var(--ink);margin-top:30px}
.director.chair h4{color:var(--green)}
.director p{font-size:15px;color:var(--text);margin-top:6px}

/* projects */
.tile{top:3063px;height:392px}
.tile-card{background:linear-gradient(180deg,#3c3e40,#5a5c5e);color:var(--white);padding:30px 33px;font-size:21px;line-height:36px}

/* clients */
.clients{left:100px;top:3595px;width:1000px;height:142px;background:var(--light);display:flex;align-items:center;justify-content:space-around;padding:0 40px}
.client{font-size:27px;font-weight:500;color:#5d6063}

/* footer */
.site-footer{left:0;top:3793px;width:1200px;height:561px;background:var(--ash)}
.contact-label{font-size:21px;font-weight:700;color:var(--white)}
.contact-line{display:flex;align-items:center;gap:16px;font-size:19px;color:var(--white)}
.field{border-bottom:2px solid #cfd0d1;font-size:12.5px;color:var(--white);padding-bottom:26px}
.copyright{left:111px;top:4325px;font-size:13px;color:var(--white)}
.rule{left:111px;top:4313px;width:1038px;height:1px;background:#8a8c8e}
</style>
</head>
<body>

<header class="site-header abs">
  <div class="logo-area abs"><div class="logo abs">KPFT</div></div>
  <nav class="main-nav abs">
    <span class="active">Home</span><span>Who we are</span><span>Vision</span><span>Mission</span><span>Directors</span><span>Values</span><span>Contact Us</span>
    <span class="nav-phone"><svg width="14" height="14" viewBox="0 0 24 24"><path fill="#fff" d="M6.6 10.8a15 15 0 0 0 6.6 6.6l2.2-2.2c.3-.3.7-.4 1-.2 1.1.4 2.3.6 3.6.6.6 0 1 .4 1 1V20c0 .6-.4 1-1 1C10.6 21 3 13.4 3 4c0-.6.4-1 1-1h3.5c.6 0 1 .4 1 1 0 1.3.2 2.5.6 3.6.1.3 0 .7-.2 1z"/></svg>+1 888 888 8888</span>
  </nav>
</header>

<section class="hero abs" role="img" aria-label="Photo of two consultants reviewing a tablet in a modern glass office"></section>
<div class="hero-text abs">
  <p class="hero-welcome">Welcome To</p>
  <h1 class="hero-title">Project &amp; <span>Cost</span><br><span>Management</span><br>Consultancy</h1>
  <p class="hero-lead">Excepteur sint occaecat cupidatat non proident,<br>sunt in culpa qui officia deserunt mollit anim id</p>
  <a class="btn btn-green">Get Started</a>
</div>
<div class="dots abs"><i></i><i class="on"></i><i></i></div>

<div class="counter counter-projects abs">Number Of Projects 300+</div>
<div class="counter counter-value abs">Total Value : AED 25M</div>

<h2 class="heading abs" style="left:111px;top:752px">Who <span>We Are</span></h2>
<div class="section-text abs" style="top:810px">
  <p>Sed ut perspiciatis unde omnis iste natus error sit voluptatem accusantium doloremque laudantium, totam rem aperiam, eaque ipsa quae ab illo inventore veritatis et quasi architecto beatae vitae dicta sunt explicabo. Nemo enim ipsam voluptatem quia voluptas sit aspernatur aut odit aut fugit, sed quia consequuntur magni dolores eos qui ratione voluptatem sequi nesciunt.</p>
  <p style="margin-top:10px">Neque porro quisquam est, qui dolorem ipsum quia dolor sit amet, consectetur, adipisci velit, sed quia non numquam eius modi tempora incidunt ut labore et dolore magnam aliquam quaerat voluptatem. Ut enim ad minima veniam, quis nostrum exercitationem ullam corporis suscipit laboriosam, nisi ut aliquid ex ea commodi consequatur? Quis autem vel eum iure reprehenderit qui in ea voluptate velit esse quam nihil</p>
</div>
<a class="btn btn-ash abs" style="left:111px;top:1018px">Read More</a>

<h2 class="heading abs" style="left:111px;top:1145px">Our <span>Vision</span></h2>
<div class="section-text abs" style="top:1218px">
  <p><span class="quote">“</span>&nbsp; Sed ut perspiciatis unde omnis iste natus error sit voluptatem accusantium doloremque laudantium, totam rem aperiam, eaque ipsa quae ab illo inventore veritatis et quasi architecto beatae vitae dicta sunt explicabo. Nemo enim ipsam voluptatem quia voluptas sit aspernatur aut odit aut fugit, sed quia consequuntur magni dolores eos qui ratione voluptatem sequi nesciunt. <span class="quote">”</span></p>
</div>

<h2 class="heading abs" style="left:111px;top:1382px">Our <span>Mission</span></h2>
<div class="section-text abs" style="top:1455px">
  <p><span class="quote">“</span>&nbsp; Sed ut perspiciatis unde omnis iste natus error sit voluptatem accusantium doloremque laudantium, totam rem aperiam, eaque ipsa quae ab illo inventore veritatis et quasi architecto beatae vitae dicta sunt explicabo. Nemo enim ipsam voluptatem quia voluptas sit aspernatur aut odit aut fugit, sed quia consequuntur magni dolores eos qui ratione voluptatem sequi nesciunt.Sed ut perspiciatis unde omnis iste natus error sit voluptatem accusantium doloremque laudantium, totam rem aperiam, eaque ipsa quae ab illo inventore veritatis et quasi architecto beatae vitae dicta sunt explicabo. <span class="quote">”</span></p>
</div>

<section class="values abs">
  <h2 class="heading abs" style="left:111px;top:53px;color:#fff">Our <span>Values</span></h2>
  <div class="value abs" style="left:95px;top:128px">
    <h3><svg width="60" height="56" viewBox="0 0 60 56" fill="none" stroke="#fff" stroke-width="1.6"><circle cx="30" cy="10" r="7"/><path d="M18 36c0-8 5-14 12-14s12 6 12 14"/><path d="M6 44l4-3 4 3-1-5 3-3h-5l-1-4-2 4H3l3 3zM26 50l4-3 4 3-1-5 3-3h-5l-1-4-2 4h-5l3 3zM46 44l4-3 4 3-1-5 3-3h-5l-1-4-2 4h-5l3 3z"/></svg>Experience and Expertise</h3>
    <p>Look for a firm with a proven track record in managing projects and costs in your industry.</p>
  </div>
  <div class="value abs" style="left:463px;top:128px">
    <h3><svg width="48" height="56" viewBox="0 0 48 56" fill="none" stroke="#fff" stroke-width="1.6"><path d="M4 52h40M8 52V38h8v14M20 52V30h8v22M32 52V22h8v30M8 30l12-10 8 6 14-14M36 12h6v6"/></svg>Reputation and References</h3>
    <p>Seek recommendations and check references to ensure reliability and effectiveness.</p>
  </div>
  <div class="value abs" style="left:832px;top:128px">
    <h3><svg width="50" height="56" viewBox="0 0 50 56" fill="none" stroke="#fff" stroke-width="1.6"><circle cx="26" cy="14" r="8"/><circle cx="26" cy="14" r="3"/><path d="M4 44l10-6h12a3 3 0 0 1 0 6h-8M26 44l14-8a3 3 0 0 1 4 4L30 50H4"/></svg>Services Offered</h3>
    <p>Ensure the consultancy offers comprehensive services that match your specific needs.</p>
  </div>
  <div class="value abs" style="left:95px;top:290px">
    <h3><svg width="60" height="56" viewBox="0 0 60 56" fill="none" stroke="#fff" stroke-width="1.6"><rect x="4" y="14" width="12" height="10"/><rect x="40" y="14" width="12" height="10"/><rect x="22" y="34" width="12" height="10"/><path d="M16 19h24M10 24v15h12M46 24v15H34"/></svg>Methodologies</h3>
    <p>Look for a firm with a proven track record in managing projects and costs in your industry.</p>
  </div>
  <div class="value abs" style="left:463px;top:290px">
    <h3><svg width="48" height="56" viewBox="0 0 48 56" fill="none" stroke="#fff" stroke-width="1.6"><circle cx="24" cy="10" r="7"/><path d="M24 17v8M8 25h32M8 25v10M24 25v10M40 25v10"/><circle cx="8" cy="41" r="5"/><rect x="19" y="36" width="10" height="10"/><circle cx="40" cy="41" r="5"/></svg>Cost Structure</h3>
    <p>Seek recommendations and check references to ensure reliability and effectiveness.</p>
  </div>
</section>

<h2 class="heading abs" style="left:0;width:1200px;text-align:center;top:2225px">Our <span>Directors</span></h2>
<div class="director abs" style="left:120px;top:2314px"><div class="photo" role="img" aria-label="Portrait of director"></div><h4>Omar Haddad</h4><p>BOARD MEMBER</p></div>
<div class="director abs" style="left:368px;top:2314px"><div class="photo" role="img" aria-label="Portrait of vice chairman"></div><h4>Yusuf Rahman</h4><p>VICE CHAIRMAN</p></div>
<div class="director chair abs" style="left:616px;top:2314px"><div class="photo" role="img" aria-label="Portrait of chairman"></div><h4>Tariq Saleh</h4><p>CHAIRMAN</p></div>
<div class="director abs" style="left:864px;top:2314px"><div class="photo" role="img" aria-label="Portrait of director"></div><h4>Rami Aziz</h4><p>BOARD MEMBER</p></div>
<div class="director abs" style="left:120px;top:2649px"><div class="photo" role="img" aria-label="Portrait of director"></div><h4>Faisal Nouri</h4><p>BOARD MEMBER</p></div>
<div class="director abs" style="left:368px;top:2649px"><div class="photo" role="img" aria-label="Portrait of director"></div><h4>Hamza Qasim</h4><p>BOARD MEMBER</p></div>
<div class="director abs" style="left:616px;top:2649px"><div class="photo" role="img" aria-label="Portrait of director"></div><h4>Idris Karam</h4><p>BOARD MEMBER</p></div>
<div class="director abs" style="left:864px;top:2649px"><div class="photo" role="img" aria-label="Portrait of director"></div><h4>Bilal Sami</h4><p>BOARD MEMBER</p></div>

<h2 class="heading abs" style="left:0;width:1200px;text-align:center;top:2992px">Our <span>Projects</span></h2>
<div class="tile abs" style="left:0;width:387px;background:linear-gradient(160deg,#dfe6ee,#6d8aa6 55%,#2e4a66)" role="img" aria-label="Photo of glass skyscrapers viewed from below"></div>
<div class="tile tile-card abs" style="left:393px;width:419px" role="img" aria-label="Photo of a lit road tunnel">
  <p>Project 2</p>
  <p style="margin-top:16px">The standard Lorem Ipsum<br>passage, used since the 1500s</p>
</div>
<div class="tile abs" style="left:818px;width:382px;background:linear-gradient(170deg,#eaf1f8,#6f98c4 45%,#1f3f63)" role="img" aria-label="Photo of modern towers against a blue sky"></div>

<h2 class="heading abs" style="left:0;width:1200px;text-align:center;top:3540px">Our <span>Key Clients</span></h2>
<div class="clients abs">
  <span class="client">NORVEL</span><span class="client">LUMARO</span><span class="client">Cresta</span><span class="client">HALVEN</span><span class="client">ORRIN &amp; CO</span>
</div>

<footer class="site-footer abs">
  <h2 class="heading abs" style="left:111px;top:77px;color:#fff">Contact <span>Us</span></h2>
  <p class="contact-label abs" style="left:111px;top:140px">PHONE</p>
  <p class="contact-line abs" style="left:111px;top:185px"><svg width="20" height="20" viewBox="0 0 24 24"><path fill="#fff" d="M6.6 10.8a15 15 0 0 0 6.6 6.6l2.2-2.2c.3-.3.7-.4 1-.2 1.1.4 2.3.6 3.6.6.6 0 1 .4 1 1V20c0 .6-.4 1-1 1C10.6 21 3 13.4 3 4c0-.6.4-1 1-1h3.5c.6 0 1 .4 1 1 0 1.3.2 2.5.6 3.6.1.3 0 .7-.2 1z"/></svg>+1 888 888 8888</p>
  <p class="contact-label abs" style="left:111px;top:260px">MAIL</p>
  <p class="contact-line abs" style="left:111px;top:302px"><svg width="26" height="18" viewBox="0 0 26 18" fill="none" stroke="#fff" stroke-width="1.6"><rect x="1" y="1" width="24" height="16"/><path d="M1 1l12 9 12-9"/></svg>info@kpft.ae</p>
  <p class="contact-label abs" style="left:111px;top:378px">ADDRESS</p>
  <p class="contact-line abs" style="left:111px;top:418px"><svg width="18" height="24" viewBox="0 0 18 24"><path fill="#fff" d="M9 0a9 9 0 0 0-9 9c0 7 9 15 9 15s9-8 9-15a9 9 0 0 0-9-9zm0 13a4 4 0 1 1 0-8 4 4 0 0 1 0 8z"/></svg>Lorem,Ipsum,Usa -437916</p>

  <div class="field abs" style="left:488px;top:136px;width:301px">Name</div>
  <div class="field abs" style="left:848px;top:136px;width:301px">Email</div>
  <div class="field abs" style="left:488px;top:214px;width:301px">Phone</div>
  <div class="field abs" style="left:848px;top:214px;width:301px">Address</div>
  <div class="field abs" style="left:488px;top:287px;width:661px;padding-bottom:88px">Type Your Message</div>
  <a class="btn btn-green abs" style="left:483px;top:410px;margin:0;padding:12px 28px;font-size:14px">Submit Now</a>

  <div class="abs" style="left:1064px;top:540px;width:20px;height:20px;background:#fff;border-radius:3px"></div>
</footer>
<div class="rule abs"></div>
<p class="copyright abs">© 2024 &nbsp;KPFT. All rights reserved.</p>

</body>
</html>
```